Design a Website Mockup for a Clinic

first look at our existing website [url removed, login to view] , this is a clinic website and we want redesign it, we need a professional and simple mockup for it.

```html
<!DOCTYPE html>
<html lang="en">
<head>
<meta charset="utf-8">
<title>Medivale Clinic</title>
<link href="https://fonts.googleapis.com/css2?family=Roboto+Condensed:wght@400;700&family=Roboto:wght@300;400;500&display=swap" rel="stylesheet">
<style>
:root{
  --teal:#35afd3;
  --teal-dark:#2a9cbf;
  --coral:#e8695e;
  --green:#8dc63f;
  --ink:#3c3c3c;
  --muted:#8a8a8a;
  --line:#e3e3e3;
  --footer-top:#3b3b3b;
  --footer-bottom:#2c2c2c;
  --white:#fff;
}
*{box-sizing:border-box;margin:0;padding:0}
html,body{width:1200px;height:3061px;overflow:hidden}
body{font-family:"Roboto",sans-serif;color:var(--ink);background:var(--white);position:relative;font-size:10px}
.abs{position:absolute}

/* top bar */
.topbar{top:0;left:0;width:1200px;height:29px;background:var(--teal);color:var(--white);font-size:10px}
.topbar .links{left:138px;top:9px;display:flex;gap:20px}
.topbar .links span::before{content:"";display:inline-block;width:5px;height:5px;border-radius:50%;background:#fff;margin-right:5px;vertical-align:middle}
.topbar .search{left:912px;top:5px;width:155px;height:20px;background:#fff;border-radius:10px;color:#aaa;font-size:9px;padding:4px 12px}
.topbar .search svg{position:absolute;right:8px;top:5px}

/* header */
.header{top:29px;left:0;width:1200px;height:67px;border-bottom:1px solid var(--line)}
.logo{left:133px;top:19px;display:flex;align-items:center;gap:8px;font-family:"Roboto Condensed",sans-serif;font-weight:700;font-size:27px;color:var(--teal);letter-spacing:1px}
.logo i{width:16px;height:16px;background:var(--teal);display:block}
.nav{left:372px;top:14px;display:flex;font-size:11.5px;color:#555}
.nav span{padding:0 11px;height:38px;line-height:38px}
.nav .active{background:var(--teal);color:#fff}

/* hero */
.hero{top:96px;left:0;width:1200px;height:376px;background:linear-gradient(100deg,#7fa9cf 0%,#a9cbe8 35%,#c9e0f2 60%,#8fc6c0 85%,#5fa9a3 100%)}
.hero .tag{left:88px;top:124px;background:#fff;padding:7px 16px;font-family:"Roboto Condensed",sans-serif;font-weight:700;font-size:18px;color:var(--teal)}
.hero .sub{left:88px;top:166px;width:560px;height:33px;background:rgba(255,255,255,.75);font-size:9px;padding:11px 16px;color:#555}
.hero .btn{left:88px;top:213px;width:127px;height:40px;background:var(--coral);color:#fff;font-family:"Roboto Condensed",sans-serif;font-weight:700;font-size:13px;line-height:40px;text-align:center}
.sidetools{right:0;top:207px;width:36px}
.sidetools div{height:34px;margin-bottom:3px;background:#555;display:flex;align-items:center;justify-content:center}
.sidetools div:first-child{background:var(--teal)}

/* features */
.feature{top:504px;width:216px;height:212px;border:1px solid var(--line);text-align:center}
.feature .icon{width:60px;height:60px;border-radius:50%;background:var(--teal);margin:23px auto 0;display:flex;align-items:center;justify-content:center}
.feature h3{font-family:"Roboto Condensed",sans-serif;font-size:15px;margin-top:19px;color:#333}
.feature p{font-size:9px;color:var(--muted);line-height:17.5px;margin:6px 14px 0}
.hours{font-size:9px;color:var(--muted);margin:6px 16px 0;text-align:left;line-height:19px}
.hours div{display:flex}
.hours .dots{flex:1;border-bottom:1px dotted #bbb;margin:0 3px 6px}

/* section titles */
.sec-title{font-family:"Roboto Condensed",sans-serif;font-weight:700;font-size:18px;color:var(--teal)}
.sec-sub{font-size:9px;color:var(--muted)}

/* specialists */
.photo{background:linear-gradient(160deg,#e6eef2,#c9d8e0)}
.doctor{top:801px;width:297px}
.doctor .photo{height:298px}
.doctor h4{font-weight:400;font-size:13px;margin-top:10px;color:#444}
.doctor .role{font-size:9.5px;color:var(--muted);margin-top:8px}
.doctor p{font-size:9px;color:#777;line-height:17px;margin-top:9px}
.social{display:flex;gap:5px;margin-top:12px}
.social i{width:18px;height:18px;border-radius:50%;background:#555;display:block}
.arrow-box{width:22px;height:22px;border:1px solid var(--line);background:#fff;display:flex;align-items:center;justify-content:center}

/* banners */
.banner{top:1268px;height:157px}
.banner .copy{color:#fff}
.banner h5{font-family:"Roboto",sans-serif;font-weight:400;font-size:17px}
.banner p{font-size:9px;line-height:18px;margin-top:6px;opacity:.9}
.banner .btn{background:var(--green);color:#fff;font-size:8px;font-weight:500;padding:7px 20px;display:inline-block;margin-top:10px}

/* news */
.news{top:1501px;width:295px}
.news .photo{height:203px}
.news h4{font-weight:400;font-size:12px;margin-top:16px;color:#444}
.news .meta{font-size:8px;color:#aaa;margin-top:8px}
.news p{font-size:9px;color:#777;line-height:15px;margin-top:10px}

/* appointment */
.appoint{top:1855px;left:0;width:1200px;height:382px;background:linear-gradient(90deg,#4a5866 0%,#56697a 55%,#7c8d98 80%,#8c9aa2 100%)}
.appoint h2{position:absolute;top:66px;width:1200px;text-align:center;font-family:"Roboto Condensed",sans-serif;font-size:18px;color:#fff;font-weight:700}
.appoint .intro{position:absolute;top:98px;left:180px;width:840px;text-align:center;font-size:9px;color:#e8eef2;line-height:18px}
.field{left:349px;width:242px;height:35px;background:#fff;font-size:9px;color:#aaa;display:flex;align-items:center}
.field .ic{width:38px;height:100%;border-right:1px solid #eee;display:flex;align-items:center;justify-content:center;margin-right:10px}
.submit{left:349px;top:278px;width:242px;height:36px;background:var(--coral);color:#fff;font-family:"Roboto Condensed",sans-serif;font-weight:700;font-size:13px;text-align:center;line-height:36px}
.message{left:600px;top:145px;width:251px;height:169px;background:#fff;font-size:9px;color:#aaa;padding:10px}

/* info columns */
.col{top:2280px}
.col-title{font-family:"Roboto Condensed",sans-serif;font-weight:700;font-size:18px;color:var(--teal)}
.pager{display:flex;gap:4px}
.pager i{width:16px;height:4px;background:#ccc;display:block}
.pager .on{background:var(--teal)}
.faq-open{margin-top:24px;border-top:1px solid var(--line);padding-top:10px}
.faq-q{display:flex;align-items:center;gap:12px;font-size:12px;color:#444}
.faq-q i{width:15px;height:15px;background:var(--teal);color:#fff;font-style:normal;font-size:12px;line-height:14px;text-align:center}
.faq-q.closed i{background:#ccc}
.faq-a{font-size:9px;color:#777;line-height:17.5px;margin:12px 0 14px}
.faq-row{border-top:1px solid var(--line);padding:10px 0 10px}
.testi{display:flex;gap:18px;margin-top:28px}
.testi .photo{width:86px;height:86px;flex:none}
.testi p{font-size:9px;font-style:italic;color:#888;line-height:19px}
.testi .who{color:var(--teal);font-size:11px;margin-top:10px}
.tweet{font-size:9px;color:#777;line-height:16px;margin-top:14px;border-bottom:1px solid #f0f0f0;padding-bottom:10px}
.tweet .date{font-size:8px;color:#aaa}
.tweet a{color:var(--teal);text-decoration:none}
.tweet .acts{color:#aaa;font-size:8px;margin-top:10px;display:flex;gap:22px}

/* footer */
.foot-top{top:2648px;left:0;width:1200px;height:152px;background:var(--footer-top);color:#ccc}
.foot-logo{left:133px;top:32px;display:flex;align-items:center;gap:10px;font-family:"Roboto Condensed",sans-serif;font-weight:700;font-size:32px;color:#fff;letter-spacing:1px}
.foot-logo i{width:20px;height:20px;background:#fff;display:block}
.foot-about{left:372px;top:28px;width:350px;font-size:9px;line-height:17.5px}
.foot-social{left:372px;top:88px;display:flex;gap:8px}
.foot-social i{width:26px;height:26px;background:#5c5c5c;display:block}
.newsletter{left:771px;top:22px;width:300px}
.newsletter h4{font-family:"Roboto Condensed",sans-serif;font-size:18px;color:#fff}
.newsletter p{font-size:9px;line-height:17px;margin-top:6px}
.nl-form{display:flex;margin-top:14px}
.nl-form span{width:204px;height:28px;background:#fff;color:#aaa;font-size:8px;padding:9px}
.nl-form b{width:87px;height:28px;background:var(--teal);color:#fff;font-family:"Roboto Condensed",sans-serif;font-size:11px;text-align:center;line-height:28px}
.divider-v{left:747px;top:22px;width:1px;height:110px;background:#555}
.foot-bottom{top:2800px;left:0;width:1200px;height:261px;background:var(--footer-bottom);color:#aaa}
.fcol{top:28px;width:200px;font-size:9px;line-height:24px}
.fcol h6{font-family:"Roboto",sans-serif;font-weight:400;font-size:12px;color:#fff;margin-bottom:6px}
.fcol b{color:#ddd;font-weight:500}
.copyright{top:185px;left:133px;width:934px;border-top:1px solid #3e3e3e;padding-top:16px;text-align:center;font-size:9px;line-height:17px}
</style>
</head>
<body>

<div class="abs topbar">
  <div class="abs links"><span>English</span><span>Register</span><span>Login</span></div>
  <div class="abs search">Search
    <svg width="10" height="10" viewBox="0 0 10 10"><circle cx="4" cy="4" r="3" fill="none" stroke="#666" stroke-width="1.2"/><line x1="6.3" y1="6.3" x2="9" y2="9" stroke="#666" stroke-width="1.2"/></svg>
  </div>
</div>

<header class="abs header">
  <div class="abs logo"><i></i>MEDIVALE</div>
  <nav class="abs nav">
    <span class="active">Home</span><span>Explore ⌄</span><span>Shortcodes</span><span>Bonus Pages ⌄</span><span>Blog Hub ⌄</span><span>Doctors ⌄</span><span>Medical Services ⌄</span>
  </nav>
</header>

<section class="abs hero" role="img" aria-label="Surgical team in scrubs and masks working in an operating room">
  <div class="abs tag">24 HOURS SERVICE</div>
  <div class="abs sub">Proin gravida nibh vel velit auctor aliquet. Class aptent taciti sociosqu ad litora torquent per conubia</div>
  <div class="abs btn">READ MORE</div>
  <div class="abs sidetools">
    <div><svg width="14" height="14" viewBox="0 0 14 14"><path d="M3 11 L8 6 M9 2 a3 3 0 1 0 3 3 l-2 0 0-2z" stroke="#fff" stroke-width="2" fill="none"/></svg></div>
    <div><svg width="14" height="14" viewBox="0 0 14 14"><path d="M2 5h3l6-3v10l-6-3H2z" fill="#fff"/></svg></div>
    <div><svg width="14" height="14" viewBox="0 0 14 14"><circle cx="7" cy="3" r="1.4" fill="#fff"/><rect x="6" y="6" width="2" height="6" fill="#fff"/></svg></div>
  </div>
</section>

<div class="abs feature" style="left:133px">
  <div class="icon"><svg width="34" height="34" viewBox="0 0 34 34"><circle cx="17" cy="17" r="14" fill="none" stroke="#fff" stroke-width="3"/><text x="17" y="22" text-anchor="middle" font-size="13" font-weight="700" fill="#fff" font-family="Roboto,sans-serif">24</text></svg></div>
  <h3>24 HOURS SERVICE</h3>
  <p>Cum sociis natoque penatibus et magnis dis parturient montes mus. Pro vel nibh et elit mollis commodo et nec augue tristique sed Pro vel nibh et elit mollis commodo</p>
</div>
<div class="abs feature" style="left:372px">
  <div class="icon"><svg width="30" height="30" viewBox="0 0 30 30"><circle cx="20" cy="8" r="5" fill="#fff"/><rect x="5" y="14" width="16" height="8" rx="4" fill="#fff"/></svg></div>
  <h3>OPENING HOURS</h3>
  <div class="hours">
    <div><span>Monday – Friday</span><span class="dots"></span><span>8.30am - 5.00pm</span></div>
    <div><span>Saturday</span><span class="dots"></span><span>9.30am - 5.30pm</span></div>
    <div><span>Sunday</span><span class="dots"></span><span>9.00am - 6.00pm</span></div>
  </div>
</div>
<div class="abs feature" style="left:611px">
  <div class="icon"><svg width="28" height="28" viewBox="0 0 28 28"><rect x="4" y="5" width="20" height="19" rx="2" fill="none" stroke="#fff" stroke-width="2"/><path d="M9 15l4 4 7-8" stroke="#fff" stroke-width="2" fill="none"/></svg></div>
  <h3>CHILD CARE</h3>
  <p>Cum sociis natoque penatibus et magnis dis parturient montes mus. Pro vel nibh et elit mollis commodo et nec augue tristique sed Pro vel nibh et elit mollis commodo</p>
</div>
<div class="abs feature" style="left:850px">
  <div class="icon"><svg width="28" height="28" viewBox="0 0 28 28"><rect x="11" y="3" width="6" height="15" rx="3" fill="none" stroke="#fff" stroke-width="2"/><circle cx="14" cy="21" r="4.5" fill="#fff"/></svg></div>
  <h3>STETHOSCOPE</h3>
  <p>Cum sociis natoque penatibus et magnis dis parturient montes mus. Pro vel nibh et elit mollis commodo et nec augue tristique sed Pro vel nibh et elit mollis commodo</p>
</div>

<h2 class="abs sec-title" style="top:745px;left:0;width:1200px;text-align:center">MEET OUR MEDICAL SPECIALISTS</h2>
<p class="abs sec-sub" style="top:773px;left:0;width:1200px;text-align:center">Lorem ipsum dolor sit amet, consectetuer adipiscing elit, sed diam nonummy nibh euismod tincidunt ut laoreet dolore magna aliquam erat volutpat</p>

<div class="abs arrow-box" style="left:123px;top:938px"><svg width="6" height="8"><path d="M5 0L1 4l4 4" stroke="#bbb" fill="none"/></svg></div>
<div class="abs arrow-box" style="left:1054px;top:938px"><svg width="6" height="8"><path d="M1 0l4 4-4 4" stroke="#bbb" fill="none"/></svg></div>

<article class="abs doctor" style="left:135px">
  <div class="photo" role="img" aria-label="Smiling female nurse in blue scrubs holding a clipboard"></div>
  <h4>Cibus Eu Laoreet</h4><div class="role">Senior Doctor</div>
  <p>Suspendisse at libero porttitor nisi aliquet vulputate vitae at velit. Aliquam eget arcu magna, vel congue dui. Nunc auctor mauris tempor leo aliquam vel porta ante sodales. Nulla facilisi.</p>
  <div class="social"><i></i><i></i><i></i><i></i></div>
</article>
<article class="abs doctor" style="left:452px">
  <div class="photo" role="img" aria-label="Female doctor in white coat holding a tablet"></div>
  <h4>Pes Pede Elit</h4><div class="role">Senior Doctor</div>
  <p>Suspendisse at libero porttitor nisi aliquet vulputate vitae at velit. Aliquam eget arcu magna, vel congue dui. Nunc auctor mauris tempor leo aliquam vel porta ante sodales. Nulla facilisi.</p>
  <div class="social"><i></i><i></i><i></i><i></i></div>
</article>
<article class="abs doctor" style="left:767px">
  <div class="photo" role="img" aria-label="Male doctor in white coat with stethoscope"></div>
  <h4>Kara Senver Munst Onvase</h4><div class="role">Senior Doctor</div>
  <p>Rance fanceus eu laoreet nunc. Tincidunt nulla a Nulla eu convallis scelerisque socis nulla interdum et. Cursus senectus alique maken chika. Donec ac ante in erat dictum adipiscing.</p>
  <div class="social"><i></i><i></i><i></i><i></i></div>
</article>

<div class="abs banner" style="left:133px;width:455px;background:linear-gradient(180deg,#5c9fd4 0%,#8fc1e6 55%,#7aa35a 100%)" role="img" aria-label="Family sitting together on grass under a blue sky">
  <div class="abs copy" style="right:32px;top:24px;text-align:right;width:200px">
    <h5>Lorem Ipsum is simply</h5>
    <p>Lorem ipsum dolor sit amet, consect etur adipiscing elit, sed do eiusmod tempor incididunt</p>
    <span class="btn">VIEW DETAILS</span>
  </div>
</div>
<div class="abs banner" style="left:612px;width:453px;background:linear-gradient(180deg,#4f8fc4 0%,#9cc8e4 55%,#6e9a48 100%)" role="img" aria-label="Parents and child walking in a sunny field">
  <div class="abs copy" style="left:92px;top:24px;width:170px">
    <h5>We create healthy families</h5>
    <p>call or make an appointment online to get started</p>
    <span class="btn">VIEW DETAILS</span>
  </div>
</div>

<h2 class="abs sec-title" style="top:1450px;left:133px">LATEST NEWS</h2>
<div class="abs arrow-box" style="left:1016px;top:1458px;width:20px;height:20px"><svg width="6" height="8"><path d="M5 0L1 4l4 4" stroke="#bbb" fill="none"/></svg></div>
<div class="abs arrow-box" style="left:1041px;top:1458px;width:20px;height:20px"><svg width="6" height="8"><path d="M1 0l4 4-4 4" stroke="#bbb" fill="none"/></svg></div>

<article class="abs news" style="left:133px">
  <div class="photo" role="img" aria-label="Nurse handing a glass of water to a patient in bed"></div>
  <h4>Integer egestas lectus egestas erat</h4>
  <div class="meta">Super User, Friday, 14 November 2014</div>
  <p>Suspendisse at libero porttitor nisi aliquet vulputate vitae at velit. Aliquam eget arcu magna, vel congue dui. Nunc auctor mauris tempor leo aliquam vel porta ante sodales. Nulla facilisi. In ...</p>
</article>
<article class="abs news" style="left:452px">
  <div class="photo" role="img" aria-label="Group of medical staff in blue scrubs applauding"></div>
  <h4>Vestibulum sit amet libero ante</h4>
  <div class="meta">Super User, Friday, 14 November 2014</div>
  <p>Suspendisse at libero porttitor nisi aliquet vulputate vitae at velit. Aliquam eget arcu magna, vel congue dui. Nunc auctor mauris tempor leo aliquam vel porta ante sodales. Nulla facilisi. In ...</p>
</article>
<article class="abs news" style="left:771px">
  <div class="photo" role="img" aria-label="Doctor greeting an older couple in a clinic"></div>
  <h4>Aenean auctor wisi et um porttitor</h4>
  <div class="meta">Super User, Monday, 13 July 2015</div>
  <p>Suspendisse at libero porttitor nisi aliquet vulputate vitae at velit. Aliquam eget arcu magna, vel congue dui. Nunc auctor mauris tempor leo aliquam vel porta ante sodales. Nulla facilisi. In ...</p>
</article>

<section class="abs appoint" role="img" aria-label="Doctor in white coat at a desk, softly blurred behind the form">
  <h2>MAKE AN APPOINTMENT</h2>
  <p class="intro">Lorem ipsum dolor sit amet, consectetur adipiscing elit. Donec nec eros eget nisl fringilla commodo. Maecenas ornare, augue ut ultricies tristique, enimlectus pretium quam, quis bibendum metus tellus sed magna. Donec eu dolor. Lorem ipsum dolor sit amet, consectetur adipiscing elit. Donec nec eros eget nisl fringilla commodo</p>
  <div class="abs field" style="top:145px"><span class="ic"><svg width="11" height="11"><circle cx="5.5" cy="3" r="2.5" fill="#999"/><path d="M1 11a4.5 4 0 0 1 9 0z" fill="#999"/></svg></span>Name</div>
  <div class="abs field" style="top:189px"><span class="ic"><svg width="12" height="9"><rect width="12" height="9" fill="#999"/><path d="M0 0l6 5 6-5" stroke="#fff" fill="none"/></svg></span>Your Email</div>
  <div class="abs field" style="top:233px"><span class="ic"><svg width="12" height="10"><rect y="2" width="12" height="8" fill="#999"/><rect x="4" width="4" height="3" fill="#999"/></svg></span>Subject</div>
  <div class="abs submit">SUBMIT</div>
  <div class="abs message">Message ...</div>
</section>

<div class="abs col" style="left:133px;width:296px">
  <h3 class="col-title">FAQs</h3>
  <div class="faq-open">
    <div class="faq-q"><i>–</i>Biza sima poka Cras mattis dena?</div>
    <p class="faq-a">Class aptent taciti sociosqu ad litora torquent per conubia nostra, per inceptos himenaeos. Nullam sed sapien ipsum. Pellentesque ac eros eu mauris suscipit fermentum et sed lacus. Sed sodales mollis sagittis. Donec mattis, sapien id ornare interdum, orci nibh egestas nulla, at consectetur nunc libero eget nunc. Sed dignissim nisl at diam</p>
  </div>
  <div class="faq-row"><div class="faq-q closed"><i>+</i>Cibus eu laoreet massa?</div></div>
  <div class="faq-row"><div class="faq-q closed"><i>+</i>Nal pede elit nibh caten?</div></div>
  <div class="faq-row"><div class="faq-q closed"><i>+</i>Seni senectus aliquet pretium?</div></div>
</div>

<div class="abs col" style="left:452px;width:292px">
  <div style="display:flex;justify-content:space-between;align-items:center"><h3 class="col-title">TESTIMONIAL</h3><div class="pager"><i></i><i class="on"></i><i></i></div></div>
  <div class="testi">
    <div class="photo" role="img" aria-label="Nurse in blue scrubs"></div>
    <div><p>Chikan mipa auctor mauris ut dui luctus semper. In hac habitasse platea dictumst. Ut wisi enim ad minim veniam, quis nostrud exerci tation ullamcorper dolore magna aliquam</p><div class="who">Daniel Marsh</div></div>
  </div>
  <div class="testi" style="margin-top:22px">
    <div class="photo" role="img" aria-label="Two doctors talking in a clinic"></div>
    <div><p>Muzan auctor mauris ut dui luctus semper. In hac habitasse platea dictumst. dolore magna aliquam erat volutpat. Ut wisi enim ad minim veniam, quis nostrud</p><div class="who">Robbie</div></div>
  </div>
</div>

<div class="abs col" style="left:771px;width:294px">
  <div style="display:flex;justify-content:space-between;align-items:center"><h3 class="col-title">LATEST TWEETS</h3><div class="pager"><i class="on"></i><i></i><i></i></div></div>
  <div class="tweet"><div class="date">31 December 2014</div>25 Best Premium Clinic Templates in 2014 <a>mdv.example/t5OQwR3L</a> via <a>@medivalenews</a><div class="acts"><span>↪ Reply</span><span>⇄ Retweet</span><span>★ Favorite</span></div></div>
  <div class="tweet"><div class="date">30 December 2014</div>Are you heard about our Clinic template? Do you want to explore it more? Check here! <a>mdv.example/8Z4iF6d mdv.example/ktoUTAy</a><div class="acts"><span>↪ Reply</span><span>⇄ Retweet</span><span>★ Favorite</span></div></div>
  <div class="tweet" style="border:0"><div class="date">29 December 2014</div>Just few days to get 30% OFF store-wide &amp; Extra 3 Months of Subscription. Be quick! <a>mdv.example/EjF07RNQ</a> via <a>@medivalenews</a><div class="acts"><span>↪ Reply</span><span>⇄ Retweet</span><span>★ Favorite</span></div></div>
</div>

<footer>
  <div class="abs foot-top">
    <div class="abs foot-logo"><i></i>MEDIVALE</div>
    <p class="abs foot-about">Lorem ipsum dolor sit amet, consectetur adipiscing elit. Donec nec eros eget nisl fringilla commodo. Maecenas ornare, augue ut ultricies tristique, enimlectus pretium quam quis bibendum metus tellus sed magna. Donec eu dolor.</p>
    <div class="abs foot-social"><i></i><i></i><i></i><i></i><i></i></div>
    <div class="abs divider-v"></div>
    <div class="abs newsletter">
      <h4>NEWSLETTER</h4>
      <p>Lorem ipsum dolor sit amet, consectetur adipiscing elit. Donec nec eros eget nisl fringilla commodo.</p>
      <div class="nl-form"><span>Your Email</span><b>SUBSCRIBE</b></div>
    </div>
  </div>
  <div class="abs foot-bottom">
    <div class="abs fcol" style="left:133px">
      <h6>CONTACT &amp; SUPPORT</h6>
      <div><b>Address :</b> No 18 Larkfield Row 22/4 Riverton,<br>Eastshire</div>
      <div><b>Email :</b> care@medivale.example</div>
      <div><b>Phone 1 :</b> 0155 020 314</div>
      <div><b>Phone 2 :</b> 0155 020 315</div>
    </div>
    <div class="abs fcol" style="left:372px"><h6>INFORMATION</h6><div>About Us</div><div>Our Location</div><div>Contact Us</div><div>Archive Template</div><div>Our Company</div></div>
    <div class="abs fcol" style="left:611px"><h6>COMMUNITY</h6><div>Community Health &amp; Wellness</div><div>Community Relations</div><div>Community Services</div><div>Resources</div><div>Community Reports</div></div>
    <div class="abs fcol" style="left:850px"><h6>ADMISSION</h6><div>Undergraduate Courses</div><div>Graduate Courses</div><div>International Students</div><div>Lifelong Learning</div><div>Online and Distance Courses</div></div>
    <div class="abs copyright">Copyright © 2015 Medivale Clinic. All Rights Reserved. Designed by Northgrid Studio<br>Medivale CMS is Free Software released under the Open Clinic Licence.</div>
  </div>
</footer>

</body>
</html>
```